Update New Business Card - For Start Up

I need to update my business card, I have our old version for example. I would like to keep to the same colors and theme. We are a threat reporting and case management tool for corporations and educational institutions.

Target Market(s)

Corporate Security and Human Resources, School Administrators and Superintendents.

Industry/Entity Type

Physical Security and Technology.

Contact Information for Business Card

My Name, Founder/CEO, phone number 555-214-6082, Logo, Web...

Colors
0054AA
0677BA
7BADD7
CADEEF
E8F1F8

Requirements
Must have
• Something new and trendy.

```html
<!DOCTYPE html>
<html lang="en">
<head>
<meta charset="utf-8">
<title>Vantora Business Card</title>
<link rel="stylesheet" href="https://fonts.googleapis.com/css2?family=Poppins:ital,wght@0,400;0,500;0,700;1,500&display=swap">
<style>
  :root {
    --navy: #03294a;
    --brand-blue: #0054aa;
    --brand-mid: #0677ba;
    --ink: #111111;
    --white: #ffffff;
  }
  * { margin: 0; padding: 0; box-sizing: border-box; }
  html, body {
    width: 1200px;
    height: 1200px;
    overflow: hidden;
    background: var(--navy);
    font-family: "Poppins", sans-serif;
  }
  .canvas { position: relative; width: 1200px; height: 1200px; }

  .card { position: absolute; width: 680px; height: 389px; overflow: hidden; }
  .card-front { left: 258px; top: 180px; background: var(--white); }
  .card-back { left: 262px; top: 631px; background: var(--brand-blue); }

  .person-name {
    position: absolute; left: 79px; top: 107px;
    font-weight: 700; font-size: 24px; letter-spacing: -0.3px;
    color: var(--brand-blue); line-height: 1;
  }
  .person-title {
    position: absolute; left: 79px; top: 142px;
    font-style: italic; font-weight: 500; font-size: 12px;
    color: var(--ink); line-height: 1;
  }
  .contact-list { position: absolute; left: 78px; top: 217px; list-style: none; }
  .contact-item {
    display: flex; align-items: center; height: 24px; margin-bottom: 12.5px;
    font-size: 13px; color: var(--ink);
  }
  .contact-icon { width: 24px; height: 24px; margin-right: 16px; flex: none; }
  .divider { color: var(--brand-blue); margin: 0 4px; }

  .front-brand {
    position: absolute; left: 390px; top: 97px; width: 210px;
    display: flex; flex-direction: column; align-items: center;
  }
  .brand-dot { width: 120px; height: 120px; border-radius: 50%; background: var(--brand-blue); }
  .brand-name-front {
    margin-top: 18px; font-weight: 700; font-size: 26px; letter-spacing: 4px;
    color: var(--brand-blue);
  }

  .back-circle {
    position: absolute; left: 190px; top: 45px; width: 300px; height: 300px;
    border-radius: 50%; background: var(--brand-mid); opacity: 0.75;
  }
  .brand-name-back {
    position: absolute; left: 0; right: 0; top: 160px; text-align: center;
    font-weight: 500; font-size: 64px; letter-spacing: 18px; text-indent: 18px;
    color: var(--white); line-height: 1;
  }
  .website {
    position: absolute; left: 0; right: 0; top: 302px; text-align: center;
    font-weight: 400; font-size: 17px; letter-spacing: 7px; text-indent: 7px;
    color: var(--white);
  }
</style>
</head>
<body>
<main class="canvas">
  <section class="card card-front">
    <h1 class="person-name">DANA WHITCOMBE</h1>
    <p class="person-title">Chief executive officer</p>
    <ul class="contact-list">
      <li class="contact-item">
        <svg class="contact-icon" viewBox="0 0 24 24" aria-hidden="true">
          <circle cx="12" cy="12" r="12" fill="var(--brand-blue)"/>
          <path d="M12 5.5a4.3 4.3 0 0 0-4.3 4.3c0 3.2 4.3 8 4.3 8s4.3-4.8 4.3-8A4.3 4.3 0 0 0 12 5.5z" fill="#fff"/>
          <circle cx="12" cy="9.8" r="1.7" fill="var(--brand-blue)"/>
        </svg>
        12.st city country 12345
      </li>
      <li class="contact-item">
        <svg class="contact-icon" viewBox="0 0 24 24" aria-hidden="true">
          <circle cx="12" cy="12" r="12" fill="var(--brand-blue)"/>
          <path d="M8.6 6.5l1.8 0 .9 2.6-1.3 1.1c.6 1.4 1.7 2.5 3.1 3.1l1.1-1.3 2.6.9v1.8c0 .6-.5 1.1-1.1 1.1C11 15.8 7.5 12.3 7.5 7.6c0-.6.5-1.1 1.1-1.1z" fill="#fff"/>
        </svg>
        888-899-3799<span class="divider">|</span>555-214-6082
      </li>
      <li class="contact-item">
        <svg class="contact-icon" viewBox="0 0 24 24" aria-hidden="true">
          <circle cx="12" cy="12" r="12" fill="var(--brand-blue)"/>
          <rect x="6" y="8" width="12" height="8.5" rx="0.8" fill="#fff"/>
          <path d="M6.5 8.6L12 12.8l5.5-4.2M6.5 16l4-3.5M17.5 16l-4-3.5" stroke="var(--brand-blue)" stroke-width="1" fill="none"/>
        </svg>
        dana@vantora.co
      </li>
    </ul>
    <div class="front-brand">
      <div class="brand-dot"></div>
      <p class="brand-name-front">VANTORA</p>
    </div>
  </section>

  <section class="card card-back">
    <div class="back-circle"></div>
    <p class="brand-name-back">VANTORA</p>
    <p class="website">www.vantora.co</p>
  </section>
</main>
</body>
</html>
```